Red Pine Vector 1/2 Page Color Print Ad

This is a 1/2 page color print ad - no larger than 7-1/2 wide x 5 high. Please provide the ad as a high-res PDF file (preferred) or 300 dpi jpg file

Included in some way should be a description of the services Red Pine Vector LLC provides -
Red Pine Vector LLC is a Professional Information Technology Services Organization providing services in:
Strategy, Assessment, Project Management, Design, System Administration, Implementation, On-going Support and Cloud based Management Services

A logo will need to be incorporated and will be uploaded. Additionally the Red Pine Vector LLC [RPV] Web Address is www.redpinevector.net
This website will provide further insight into what RPV does as well as color schema/look/feel of existing creative design so this ad will stay within some consistent bounds of current marketing designs.
Updates

Thanks for all the submissions - we have seen some great designs and have guaranteed the project and look forward to making a decision by Tuesday. 

Thank you all for the designs and submissions.  We do appreciate it.  Our team will be discussing the designs today and a decision should be made today, tomorrow at the very latest.

Target Market(s)

Any Business person that relies on Technology to run their business and needs an IT staff and/or partner to understand and support the business goals

Industry/Entity Type

Marketing

Requirements
Must have
• Company Logo
Company Address
Phone number
Web address

This info incorporated in some way:

```html
<!DOCTYPE html>
<html lang="en">
<head>
<meta charset="utf-8">
<title>Red Pine Vector – Half Page Print Ad</title>
<link href="https://fonts.googleapis.com/css2?family=Open+Sans:wght@300;400&display=swap" rel="stylesheet">
<style>
  :root {
    --page-bg: #eceef0;
    --ad-blue: #1aa8ea;
    --ad-blue-deep: #1598d8;
    --wave-light: #5cc3f1;
    --text-white: #ffffff;
    --text-soft: #dff3fd;
    --logo-ink: #1e4f8c;
    --logo-panel: #ffffff;
  }
  * { margin: 0; padding: 0; box-sizing: border-box; }
  html, body {
    width: 900px;
    height: 1200px;
    overflow: hidden;
    background: var(--page-bg);
    font-family: "Open Sans", Arial, sans-serif;
  }
  .ad {
    position: absolute;
    left: 30px;
    top: 320px;
    width: 840px;
    height: 560px;
    background: var(--ad-blue);
    overflow: hidden;
  }
  .logo-panel {
    position: absolute;
    left: 0;
    top: 26px;
    width: 222px;
    height: 94px;
    background: var(--logo-panel);
    display: flex;
    align-items: center;
    justify-content: center;
    gap: 8px;
  }
  .logo-mark {
    width: 14px;
    height: 14px;
    background: var(--logo-ink);
  }
  .logo-name {
    font-weight: 400;
    font-size: 20px;
    color: var(--logo-ink);
    letter-spacing: 0.2px;
  }
  .services {
    position: absolute;
    left: 244px;
    top: 38px;
    width: 580px;
    font-weight: 300;
    font-size: 16.5px;
    line-height: 25px;
    color: var(--text-soft);
  }
  .headline {
    position: absolute;
    left: 180px;
    top: 182px;
    font-weight: 300;
    font-size: 58px;
    line-height: 1;
    color: var(--text-white);
    letter-spacing: 0.5px;
  }
  .data-waves {
    position: absolute;
    left: 0;
    top: 280px;
    width: 840px;
    height: 230px;
    background: linear-gradient(180deg, rgba(92,195,241,0) 0%, rgba(92,195,241,0.45) 45%, rgba(92,195,241,0.25) 100%);
  }
  .contact {
    position: absolute;
    left: 40px;
    right: 30px;
    bottom: 22px;
    display: flex;
    justify-content: space-between;
    font-weight: 300;
    font-size: 14px;
    color: var(--text-white);
  }
  .contact-group span + span { margin-left: 18px; }
</style>
</head>
<body>
  <section class="ad">
    <div class="logo-panel">
      <span class="logo-mark"></span>
      <span class="logo-name">Red Pine Vector</span>
    </div>
    <p class="services">Strategy, Assessment, Project Management, Design, System Administration, Implementation, On-going Support, Cloud based Management Services</p>
    <h1 class="headline">We means IT ocean</h1>
    <div class="data-waves" role="img" aria-label="Flowing waves made of binary digits"></div>
    <div class="contact">
      <div class="contact-group">
        <span>T : +1 888 555 0142</span>
        <span>F : +1 888 555 0142</span>
        <span>E : management@redpinevector.net</span>
      </div>
      <span class="contact-web">W : redpinevector.net</span>
    </div>
  </section>
</body>
</html>
```